Website for a web design agency

We are a website and marketing agency. We do website design, development, and well as Brindle and Quorvia advertising and analytics. We ourselves need a new website for our own brand. We are working on some designs in-house with our own designers, but we also wanted to see what outside designers would come up with.
We are starting off with the homepage, and here is the breakdown of the sections:
https://files.brindlework.example/sheet/d/7kqTr2VnPLwXeHsaMcY4oBfJzuGNtKdWiEh3Rx9pLmQb/view?mode=share
This doc also has many links to sites we have done, which you can take screenshots of for the portfolio section.
In terms of the "look" I am going for, I want to look high-end and very beautiful designs. I found this website that I like a lot that you can use some of the elements of, just as a starting point:
http://velmarkstudio.example/layouts/pixelbarn/html/ostrevo/index.html and here is another design option they have http://velmarkstudio.example/layouts/pixelbarn/html/ostrevo/index-4.html
I'm also uploading my logo. The logo matches the gold and black look from these websites, but I would be open to switching to another color scheme if needed.
This is the link to my very old website, which you can use for some of the dummy text, and a pic of myself. I will be taking more pics of myself:
https://theplumtreeandwillowgroup.example/
We need a homepage and a portfolio page right now, but if you are the winner, we will be hiring you to make additional pages.
Updates
More designs continue to come in even today, and I want to make sure no other designers are still submitting designs.
Target Market(s)
medium and large businesses owners, and non-profits
Number of Pages Required
1 page

```html
<!DOCTYPE html>
<html lang="en">
<head>
<meta charset="utf-8">
<title>Halvern Strategies — We Build Value</title>
<link rel="stylesheet" href="https://fonts.googleapis.com/css2?family=Anton&family=Poppins:wght@400;500;600&family=Dancing+Script:wght@600&display=swap">
<style>
:root{
  --gold:#f0b429;
  --ink:#111214;
  --dark:#1d1e22;
  --card:#f5f5f5;
  --text:#555;
  --muted:#8a8a8a;
  --white:#fff;
}
*{box-sizing:border-box;margin:0;padding:0}
html,body{width:1200px;height:4992px;overflow:hidden}
body{position:relative;font-family:"Poppins",sans-serif;color:var(--ink);background:var(--white)}
.abs{position:absolute}
.display{font-family:"Anton",sans-serif;font-weight:400;letter-spacing:.5px}
.brand{font-family:"Poppins",sans-serif;font-weight:600;color:var(--gold);font-size:30px;letter-spacing:3px;line-height:1}
.brand small{display:block;font-size:12px;letter-spacing:6px;margin-top:4px;font-weight:600}
.btn{position:absolute;background:var(--gold);color:var(--white);border-radius:30px;font-weight:600;display:flex;align-items:center;justify-content:center}

/* hero */
.hero{left:0;top:0;width:1200px;height:637px;overflow:hidden;background:linear-gradient(115deg,#2b3a44 0%,#1d2b33 35%,#3a2230 70%,#1b1c26 100%)}
.hero-photo{position:absolute;inset:0;background:radial-gradient(ellipse at 48% 68%,rgba(70,150,160,.55),transparent 45%),radial-gradient(ellipse at 80% 30%,rgba(120,40,70,.45),transparent 50%)}
.hero-shade{position:absolute;inset:0;background:rgba(10,12,18,.35)}
.nav{position:absolute;top:44px;left:72px;right:72px;display:flex;align-items:center}
.nav ul{list-style:none;display:flex;gap:46px;margin-left:150px;font-size:13px;color:var(--white)}
.nav ul li.active{color:var(--gold)}
.nav .phone{margin-left:auto;color:var(--white);font-size:14px;display:flex;align-items:center;gap:8px}
.hero h1{position:absolute;top:185px;width:100%;text-align:center;color:var(--white);font-size:112px;line-height:1.1}
.hero p{position:absolute;top:318px;width:100%;text-align:center;color:var(--white);font-size:25px;font-weight:500;line-height:1.4}
.hero-progress{position:absolute;left:0;bottom:0;width:1200px;height:8px;background:#5a6068}
.hero-progress span{display:block;width:208px;height:100%;background:#e9e9e9}

/* section heading */
.sec-title{width:100%;text-align:center;font-size:60px;line-height:1}
.rule{position:absolute;left:72px;width:1056px;height:2px;background:var(--ink)}

/* service cards */
.card{position:absolute;width:338px;height:388px;background:var(--card);padding:60px 10px 0 10px}
.card::after{content:"";position:absolute;left:12px;top:14px;width:345px;height:392px;border:2px solid var(--gold);border-left:none;border-top:none;z-index:-1}
.card::before{content:"";position:absolute;right:-19px;top:14px;width:12px;height:2px;background:var(--gold)}
.card h3{font-size:31px;margin:18px 0 14px;line-height:1}
.card p{font-size:13px;line-height:25px;color:var(--text)}
.card .more{margin-top:20px;margin-left:2px;color:var(--gold);font-size:15px;font-weight:500;display:flex;align-items:center;gap:10px}

/* portfolio */
.filters{position:absolute;top:1813px;right:72px;display:flex;gap:27px;font-size:12.5px;color:var(--text)}
.filters .on{color:var(--gold)}
.tile{position:absolute;width:400px;height:437px}
.tile-caption{position:absolute;left:72px;top:2606px;color:var(--white)}
.tile-caption h4{font-size:30px;margin-bottom:12px}
.tile-caption p{font-size:13.5px;line-height:24px;width:300px}

/* case studies */
.case-left{left:0;top:2795px;width:598px;height:630px;background:radial-gradient(ellipse at 60% 20%,#2a2a2a,#0c0c0c 60%)}
.case-right{left:598px;top:2795px;width:602px;height:630px;background:var(--gold)}
.quote-text{left:656px;top:3030px;font-size:42px;line-height:61px;color:var(--ink)}

/* team */
.member{position:absolute;top:3594px;width:336px}
.member .photo{height:363px}
.member .share{position:absolute;left:0;top:343px;width:40px;height:40px;background:var(--gold);display:flex;align-items:center;justify-content:center}
.member h5{font-family:"Anton",sans-serif;font-weight:400;font-size:20px;text-align:center;margin-top:22px}
.member span{display:block;text-align:center;font-size:12px;color:var(--text);margin-top:10px}

/* footer */
.footer{left:0;top:4563px;width:1200px;height:429px;background:var(--dark);color:#c9c9c9}
.fcol{position:absolute;top:78px;font-size:13px;line-height:31.5px}
.fcol h6{font-family:"Anton",sans-serif;font-weight:400;color:var(--gold);font-size:19px;line-height:1;margin-bottom:14px}
</style>
</head>
<body>

<!-- hero -->
<section class="abs hero">
  <div class="hero-photo" role="img" aria-label="Hand resting on a computer mouse on a dimly lit desk"></div>
  <div class="hero-shade"></div>
  <svg class="abs" style="left:0;top:0" width="1200" height="637" viewBox="0 0 1200 637">
    <circle cx="1208" cy="200" r="118" fill="#f0b429"/>
    <circle cx="1200" cy="200" r="175" fill="none" stroke="#d8d8d8" stroke-width="1.2" opacity=".7"/>
    <circle cx="45" cy="570" r="112" fill="#f0b429"/>
    <circle cx="40" cy="540" r="160" fill="none" stroke="#d8d8d8" stroke-width="1.2" opacity=".7"/>
  </svg>
  <nav class="nav">
    <div class="brand">HALVERN<small>STRATEGIES</small></div>
    <ul>
      <li class="active">Home</li><li>What we do</li><li>Portfolio</li><li>Testimonial</li><li>Our Team</li><li>Consultation</li>
    </ul>
    <div class="phone">
      <svg width="14" height="14" viewBox="0 0 24 24"><path fill="#f0b429" d="M6.6 10.8a15 15 0 0 0 6.6 6.6l2.2-2.2c.3-.3.7-.4 1-.2 1.1.4 2.3.6 3.6.6.6 0 1 .4 1 1V20c0 .6-.4 1-1 1A17 17 0 0 1 3 4c0-.6.4-1 1-1h3.5c.6 0 1 .4 1 1 0 1.3.2 2.5.6 3.6.1.3 0 .7-.2 1z"/></svg>
      +1 123 456 789
    </div>
  </nav>
  <h1 class="display">We Build Value</h1>
  <p>Enterprise Level Website Development<br>and Online Marketing</p>
  <div class="btn" style="left:490px;top:406px;width:220px;height:52px;font-size:15px">SEE HOW WE DO IT</div>
  <div class="hero-progress"><span></span></div>
</section>

<!-- what we do -->
<h2 class="abs display sec-title" style="top:708px">What We Do</h2>
<div class="rule" style="top:789px"></div>

<div class="card" style="left:72px;top:826px">
  <svg width="62" height="54" viewBox="0 0 62 54" fill="none" stroke="#f0b429" stroke-width="3"><rect x="2" y="2" width="58" height="40"/><path d="M22 52h18M31 42v10M20 32l18-18 4 4-18 18h-4z"/></svg>
  <h3 class="display">Websites Design</h3>
  <p>Lorem ipsum dolor sit amet, consect adipiscing elit. In convallis tincidunt libero qer. Pellentesque dictum purus odio, non bibum lectus commodo sit amet.</p>
  <div class="more">Learn More <svg width="18" height="10" viewBox="0 0 18 10" fill="none" stroke="#f0b429" stroke-width="1.6"><path d="M0 5h16M12 1l4 4-4 4"/></svg></div>
</div>
<div class="card" style="left:432px;top:826px">
  <svg width="62" height="62" viewBox="0 0 62 62" fill="none" stroke="#f0b429" stroke-width="3"><rect x="2" y="2" width="58" height="58"/><path d="M2 14h58M14 24h34v16H14zM14 48h34"/><path d="M14 40l10-10 8 8 6-5 10 7"/></svg>
  <h3 class="display">Landing Pages</h3>
  <p>Lorem ipsum dolor sit amet, consect adipiscing elit. In convallis tincidunt libero qer. Pellentesque dictum purus odio, non bibum lectus commodo sit amet.</p>
  <div class="more">Learn More <svg width="18" height="10" viewBox="0 0 18 10" fill="none" stroke="#f0b429" stroke-width="1.6"><path d="M0 5h16M12 1l4 4-4 4"/></svg></div>
</div>
<div class="card" style="left:792px;top:826px">
  <svg width="62" height="56" viewBox="0 0 62 56" fill="none" stroke="#f0b429" stroke-width="3"><rect x="2" y="2" width="58" height="52"/><path d="M2 14h58M20 42h22M24 32h14v10H24zM31 24v8"/></svg>
  <h3 class="display">Donation Pages</h3>
  <p>Lorem ipsum dolor sit amet, consect adipiscing elit. In convallis tincidunt libero qer. Pellentesque dictum purus odio, non bibum lectus commodo sit amet.</p>
  <div class="more">Learn More <svg width="18" height="10" viewBox="0 0 18 10" fill="none" stroke="#f0b429" stroke-width="1.6"><path d="M0 5h16M12 1l4 4-4 4"/></svg></div>
</div>

<div class="card" style="left:72px;top:1258px">
  <svg width="50" height="60" viewBox="0 0 50 60" fill="none" stroke="#f0b429" stroke-width="3"><path d="M2 2h46L30 28v28l-10-6V28z"/></svg>
  <h3 class="display">PPC and Funnels</h3>
  <p>Lorem ipsum dolor sit amet, consect adipiscing elit. In convallis tincidunt libero qer. Pellentesque dictum purus odio, non bibum lectus commodo sit amet.</p>
  <div class="more">Learn More <svg width="18" height="10" viewBox="0 0 18 10" fill="none" stroke="#f0b429" stroke-width="1.6"><path d="M0 5h16M12 1l4 4-4 4"/></svg></div>
</div>
<div class="card" style="left:432px;top:1258px">
  <svg width="58" height="62" viewBox="0 0 58 62" fill="none" stroke="#f0b429" stroke-width="3"><rect x="2" y="2" width="54" height="58"/><path d="M2 42h54M14 50h30M24 14l12 8-12 8z"/></svg>
  <h3 class="display">Video Marketing</h3>
  <p>Lorem ipsum dolor sit amet, consect adipiscing elit. In convallis tincidunt libero qer. Pellentesque dictum purus odio, non bibum lectus commodo sit amet.</p>
  <div class="more">Learn More <svg width="18" height="10" viewBox="0 0 18 10" fill="none" stroke="#f0b429" stroke-width="1.6"><path d="M0 5h16M12 1l4 4-4 4"/></svg></div>
</div>
<div class="card" style="left:792px;top:1258px">
  <svg width="58" height="54" viewBox="0 0 58 54" fill="none" stroke="#f0b429" stroke-width="3"><path d="M4 52V38h10v14M22 52V30h10v22M40 52V22h10v30M4 28l16-14 10 8L50 4M40 4h10v10"/></svg>
  <h3 class="display">Analytics and Optimization</h3>
  <p>Lorem ipsum dolor sit amet, consect adipiscing elit. In convallis tincidunt libero qer. Pellentesque dictum purus odio, non bibum lectus commodo sit amet.</p>
  <div class="more">Learn More <svg width="18" height="10" viewBox="0 0 18 10" fill="none" stroke="#f0b429" stroke-width="1.6"><path d="M0 5h16M12 1l4 4-4 4"/></svg></div>
</div>

<!-- portfolio -->
<h2 class="abs display" style="left:72px;top:1785px;font-size:62px;line-height:1">Portfolio</h2>
<div class="filters"><span class="on">All</span><span>Websites</span><span>Landing pages</span><span>Donation Pages</span><span>PPC and Funnels</span><span>Video marketing</span><span>Analytics and optimization</span></div>
<div class="rule" style="top:1872px"></div>

<div class="tile" style="left:0;top:1920px;background:linear-gradient(180deg,#e88a22 0%,#f0a040 35%,#2d7f8a 60%,#e9c9a0 100%)" role="img" aria-label="Orange and teal abstract paint flow"></div>
<div class="tile" style="left:400px;top:1920px;background:radial-gradient(ellipse at 50% 48%,#c9383a 0%,#4a2a3a 35%,#050505 65%)" role="img" aria-label="Red and blue betta fish on black"></div>
<div class="tile" style="left:800px;top:1920px;width:400px;background:linear-gradient(135deg,#d8c13a 0%,#e8e3d6 45%,#f2f2f2 100%)" role="img" aria-label="Hand sketching with a pen on paper"></div>
<div class="tile" style="left:0;top:2357px;background:linear-gradient(160deg,#3a3a3a,#1e1e1e)" role="img" aria-label="Tablet showing a web design layout"></div>
<div class="abs" style="left:0;top:2357px;width:400px;height:437px;background:linear-gradient(180deg,rgba(0,0,0,0) 30%,rgba(0,0,0,.75))"></div>
<div class="tile-caption">
  <h4 class="display" style="font-weight:400">Web Design</h4>
  <p>Lorem ipsum dolor sit amet, consect adipiscing elit. In convallis tincidunt libero qer. Pellentesque dictum</p>
  <div style="color:var(--gold);font-size:15px;font-weight:500;margin-top:6px;display:flex;align-items:center;gap:10px">Learn More <svg width="18" height="10" viewBox="0 0 18 10" fill="none" stroke="#f0b429" stroke-width="1.6"><path d="M0 5h16M12 1l4 4-4 4"/></svg></div>
</div>
<div class="tile" style="left:400px;top:2357px;background:linear-gradient(160deg,#6f8aa8,#8aa2bd 60%,#c8d0d8)" role="img" aria-label="White robotic hand on a blue background"></div>
<div class="tile" style="left:800px;top:2357px;background:linear-gradient(150deg,#3c3c3c,#232323)" role="img" aria-label="Dark stationery branding mockup"></div>

<!-- case studies -->
<div class="abs case-left" role="img" aria-label="Dark flowing abstract texture"></div>
<h2 class="abs display" style="left:0;width:668px;top:2950px;text-align:center;color:#fff;font-size:40px">CASE STUDIES</h2>
<p class="abs" style="left:86px;width:492px;top:3040px;text-align:center;color:#e6e6e6;font-size:17px;line-height:32px">Lorem ipsum dolor sit amet, consectetur adiscing elit, sed do eiusmod tempor incididunt ut labore et dolore magna aliqua. Quis ipsum suspendisse ultrices gravida. Risus commodo viverra maecenas accumsan lacus vel facilisis.</p>
<div class="btn" style="left:246px;top:3210px;width:176px;height:54px;font-size:15px">Read More</div>

<div class="abs case-right"></div>
<svg class="abs" style="left:656px;top:2892px" width="148" height="118" viewBox="0 0 148 118" fill="none" stroke="#111214" stroke-width="3.5"><path d="M2 2h60v62L36 116h-16l14-52H2z"/><path d="M84 2h60v62l-26 52h-16l14-52H84z"/></svg>
<div class="abs display quote-text">ORCI VARIUS NATOQUE<br>PENATIBUS ET MAGNIS<br>DIS PARTURIENT</div>
<div class="abs" style="left:656px;top:3230px;font-family:'Dancing Script',cursive;font-size:42px;color:#111214">Lorem ipsum</div>
<div class="abs" style="left:656px;top:3285px;font-size:12px;color:#2a2a2a">Managing Director</div>
<div class="abs" style="left:656px;top:3384px;width:50px;height:4px;background:#111214"></div>
<div class="abs" style="left:716px;top:3384px;width:50px;height:4px;background:#f6d27a"></div>
<div class="abs" style="left:776px;top:3384px;width:50px;height:4px;background:#f6d27a"></div>

<!-- team -->
<h2 class="abs display sec-title" style="top:3476px">Our Creative Team</h2>
<div class="rule" style="top:3558px"></div>

<div class="member" style="left:72px">
  <div class="photo" style="background:linear-gradient(180deg,#e8e8e8,#d6d6d6)" role="img" aria-label="Portrait of a smiling team member with glasses and curly hair"></div>
  <div class="share"><svg width="16" height="16" viewBox="0 0 16 16" fill="#fff"><circle cx="12" cy="3" r="2.5"/><circle cx="4" cy="8" r="2.5"/><circle cx="12" cy="13" r="2.5"/><path d="M4 8l8-5M4 8l8 5" stroke="#fff" stroke-width="1.4"/></svg></div>
  <h5>Praesent Posuere</h5><span>SEO</span>
</div>
<div class="member" style="left:432px">
  <div class="photo" style="background:linear-gradient(180deg,#ececec,#d9d4d0 70%,#1e1a22)" role="img" aria-label="Portrait of a team member with long blonde hair"></div>
  <div class="share"><svg width="16" height="16" viewBox="0 0 16 16" fill="#fff"><circle cx="12" cy="3" r="2.5"/><circle cx="4" cy="8" r="2.5"/><circle cx="12" cy="13" r="2.5"/><path d="M4 8l8-5M4 8l8 5" stroke="#fff" stroke-width="1.4"/></svg></div>
  <h5>Praesent Posuere</h5><span>SEO</span>
</div>
<div class="member" style="left:792px">
  <div class="photo" style="background:linear-gradient(180deg,#d3d6dc,#c4c9d1)" role="img" aria-label="Portrait of a smiling bearded team member"></div>
  <div class="share"><svg width="16" height="16" viewBox="0 0 16 16" fill="#fff"><circle cx="12" cy="3" r="2.5"/><circle cx="4" cy="8" r="2.5"/><circle cx="12" cy="13" r="2.5"/><path d="M4 8l8-5M4 8l8 5" stroke="#fff" stroke-width="1.4"/></svg></div>
  <h5>Praesent Posuere</h5><span>SEO</span>
</div>

<!-- consultation -->
<div class="abs" style="left:140px;top:4094px;width:480px;height:466px;background:radial-gradient(ellipse at 55% 50%,#c9c9c9 0%,#e4e4e4 40%,#fff 72%)" role="img" aria-label="Profile of a person blended with a golden geometric pattern"></div>
<h2 class="abs display" style="left:700px;top:4218px;font-size:62px;line-height:68px">Get a Free Audit<br>and Consultation</h2>
<div class="btn" style="left:702px;top:4378px;width:172px;height:52px;font-size:16px">Click Here</div>

<!-- footer -->
<footer class="abs footer">
  <div class="abs brand" style="left:72px;top:72px;font-size:32px">HALVERN<small>STRATEGIES</small></div>
  <div class="fcol" style="left:72px;top:146px;font-size:12.5px;line-height:22px">45 BC, making it over<br>Fratton, Australia</div>
  <div class="fcol" style="left:72px;top:218px;font-size:12.5px">info@halvernstrategies.example</div>
  <div class="fcol" style="left:72px;top:276px;font-size:12.5px">+1 123 456 789</div>

  <div class="fcol" style="left:344px"><h6>Quick Link</h6>Home<br>What we do<br>Portfolio<br>Testimonials<br>Our Team<br>Consultation</div>
  <div class="fcol" style="left:599px"><h6>Information</h6>Websites<br>Landing pages<br>Donation Pages<br>PPC and Funnels<br>Video marketing<br>Analytics and optimization</div>
  <div class="fcol" style="left:884px"><h6>Newsletter</h6></div>
  <div class="abs" style="left:884px;top:135px;width:244px;height:30px;border-bottom:1px solid #666;font-size:12.5px;color:#c9c9c9">Your Email
    <svg class="abs" style="right:0;top:2px" width="16" height="16" viewBox="0 0 16 16"><path fill="#f0b429" d="M15 1L1 7l5 2 2 6 7-14z"/></svg>
  </div>
  <div class="abs display" style="left:884px;top:236px;color:var(--gold);font-size:19px">Follow Us:</div>
  <svg class="abs" style="left:976px;top:240px" width="122" height="16" viewBox="0 0 122 16"><circle cx="6" cy="8" r="5" fill="#fff"/><circle cx="40" cy="8" r="5" fill="#fff"/><circle cx="78" cy="8" r="5" fill="#fff"/><circle cx="116" cy="8" r="5" fill="#fff"/></svg>
  <div class="abs" style="left:72px;top:357px;width:1056px;height:1px;background:#55565c"></div>
  <div class="abs" style="left:0;width:1200px;top:382px;text-align:center;font-size:12px;color:#9a9a9a">© 2021 <span style="color:var(--gold)">Halvern Strategies</span>. All right reserved</div>
  <div class="abs" style="left:1128px;top:372px;width:44px;height:44px;border-radius:50%;background:#111214;display:flex;align-items:center;justify-content:center">
    <svg width="14" height="20" viewBox="0 0 14 20" fill="none" stroke="#f0b429" stroke-width="2"><path d="M7 19V2M1 8l6-6 6 6"/></svg>
  </div>
</footer>

</body>
</html>
```